Business Card Design Project

Colette Marvaux logo on front of card with 'of Sydney' added in small font.
Back of card needs to include the following information :

"Pure pleasure for the discerning gentleman" (I may omit once I've seen the design)

colettemarvaux.com.au

Contact by SMS or email only :

colette@colettemarvaux.com.au
Mobile : 0483 615 204 or + 61 483 615 204

Target Market(s)

Male professionals aged 20-60.

Industry/Entity Type

Business

Requirements
Must have
• Simple, bold, stylish and elegant.

```html
<!DOCTYPE html>
<html lang="en">
<head>
<meta charset="utf-8">
<title>Colette Marvaux — Business Card</title>
<link rel="stylesheet" href="https://fonts.googleapis.com/css2?family=Gentium+Book+Plus:wght@400&family=Kaushan+Script&display=swap">
<style>
  :root {
    --page: #ffffff;
    --card-black: #000000;
    --stone: #c6c3b9;
    --ink-light: #ffffff;
    --text-font: "Gentium Book Plus", Georgia, serif;
    --script-font: "Kaushan Script", cursive;
  }
  * { margin: 0; padding: 0; box-sizing: border-box; }
  html, body {
    width: 1200px;
    height: 1200px;
    overflow: hidden;
    background: var(--page);
  }
  .canvas {
    position: relative;
    width: 1200px;
    height: 1200px;
  }

  /* Front of card */
  .card-front {
    position: absolute;
    left: 228px;
    top: 68px;
    width: 729px;
    height: 496px;
    background: var(--stone);
  }
  .front-panel {
    position: absolute;
    left: 0;
    top: 0;
    width: 100%;
    height: 367px;
    background: var(--card-black);
    display: flex;
    align-items: center;
    justify-content: center;
  }
  .brand-name {
    font-family: var(--text-font);
    font-weight: 400;
    font-size: 76px;
    letter-spacing: 1px;
    color: var(--ink-light);
    margin-top: -20px;
  }
  .location-band {
    position: absolute;
    left: 0;
    top: 402px;
    width: 100%;
    height: 94px;
    background: var(--card-black);
    display: flex;
    align-items: center;
    justify-content: center;
  }
  .location {
    font-family: var(--script-font);
    font-size: 40px;
    color: var(--ink-light);
    letter-spacing: 1px;
  }

  /* Back of card */
  .card-back {
    position: absolute;
    left: 228px;
    top: 608px;
    width: 729px;
    height: 498px;
    background: var(--stone);
  }
  .back-panel {
    position: absolute;
    left: 20px;
    top: 22px;
    width: 688px;
    height: 447px;
    background: var(--card-black);
    font-family: var(--text-font);
    color: var(--ink-light);
    font-size: 30px;
    line-height: 1;
  }
  .back-panel p { position: absolute; white-space: nowrap; }
  .tagline  { left: 100px; top: 48px; }
  .website  { left: 163px; top: 100px; }
  .contact-note { left: 100px; top: 204px; }
  .email    { left: 100px; top: 264px; }
  .mobile   { left: 100px; top: 306px; }
  .mobile-intl { left: 226px; top: 348px; }
</style>
</head>
<body>
<main class="canvas">
  <section class="card-front" aria-label="Card front">
    <div class="front-panel">
      <h1 class="brand-name">Colette Marvaux</h1>
    </div>
    <div class="location-band">
      <p class="location">of Sydney</p>
    </div>
  </section>

  <section class="card-back" aria-label="Card back">
    <div class="back-panel">
      <p class="tagline">Pure pleasure for deserning gentalment</p>
      <p class="website">colettemarvaux.com.au</p>
      <p class="contact-note">Contact by SMS or email only :</p>
      <p class="email">colette@colettemarvaux.com.au</p>
      <p class="mobile">Mobile : 0483 615 204 or</p>
      <p class="mobile-intl">+ 61 483 615 204</p>
    </div>
  </section>
</main>
</body>
</html>
```